Accounting business needs a fridge magnet design

I need a business card size design to be used as a fridge magnet.
It will need to be vertical not horizontal and it will have my logo and the services I provide listed below it.
It needs to be pleasing to the eye and catch peoples attention.
I have uploaded my current business card as a reference.
It can look totally different though, i am open to new ideas.

It will need to say:

Specialising in:
*Small Business Taxation
*Company & Trust Returns
*Financial Statements
*Partnership Taxation
*BAS preparation/lodgement
*Capital Gains Tax
*Business Start Ups
*Business Structuring
*Tax Planning

```html
<!DOCTYPE html>
<html lang="en">
<head>
<meta charset="utf-8">
<title>Clearline Tax – Fridge Magnet</title>
<link rel="stylesheet" href="https://fonts.googleapis.com/css2?family=Arimo:wght@400&family=Montserrat:wght@500&display=swap">
<style>
  :root {
    --page-bg: #424242;
    --card-light: #f4f4f6;
    --card-dark: #2a2b2d;
    --accent-blue: #15a8dd;
    --ink: #2b2b2d;
    --text-light: #f2f2f2;
    --badge-blue: #1c5aa0;
    --badge-yellow: #f4d21b;
  }
  * { box-sizing: border-box; margin: 0; padding: 0; }
  html, body {
    width: 1096px;
    height: 1200px;
    overflow: hidden;
    background: var(--page-bg);
  }
  .magnet {
    position: absolute;
    left: 284px;
    top: 140px;
    width: 527px;
    height: 921px;
    border-radius: 32px;
    overflow: hidden;
    background: var(--card-light);
  }
  .magnet-backdrop {
    position: absolute;
    inset: 0;
  }
  .brand-mark {
    position: absolute;
    left: 190px;
    top: 76px;
    width: 148px;
    height: 148px;
    border: 4px solid var(--ink);
    border-radius: 50%;
  }
  .brand-name {
    position: absolute;
    left: 0;
    width: 100%;
    top: 248px;
    text-align: center;
    font-family: "Montserrat", sans-serif;
    font-weight: 500;
    font-size: 40px;
    letter-spacing: 9px;
    padding-left: 9px;
    color: var(--ink);
  }
  .services {
    position: absolute;
    left: 53px;
    top: 428px;
    font-family: "Arimo", Arial, sans-serif;
  }
  .services-heading {
    font-size: 30px;
    font-weight: 400;
    color: var(--accent-blue);
    margin-bottom: 22px;
  }
  .service-list {
    list-style: none;
  }
  .service-item {
    display: flex;
    align-items: center;
    height: 33.6px;
    font-size: 23px;
    color: var(--text-light);
  }
  .service-tick {
    width: 21px;
    height: 21px;
    margin-right: 12px;
    flex: none;
  }
  .partner-badges {
    position: absolute;
    left: 59px;
    top: 827px;
    display: flex;
    align-items: center;
  }
  .badge-listing {
    display: flex;
    width: 142px;
    height: 61px;
  }
  .badge-listing-main { flex: 88; background: var(--badge-blue); }
  .badge-listing-side { flex: 54; background: var(--badge-yellow); }
  .badge-software {
    width: 76px;
    height: 76px;
    margin-left: 22px;
    border-radius: 50%;
    background: var(--accent-blue);
  }
</style>
</head>
<body>
  <div class="magnet">
    <svg class="magnet-backdrop" viewBox="0 0 527 921" width="527" height="921" aria-hidden="true">
      <path d="M0,346 Q270,459 527,329 L527,921 L0,921 Z" fill="var(--accent-blue)"/>
      <path d="M0,360 Q260,405 527,346" fill="none" stroke="#111" stroke-width="2"/>
      <path d="M0,372 Q280,440 527,355 L527,921 L0,921 Z" fill="var(--card-dark)"/>
    </svg>

    <div class="brand-mark"></div>
    <div class="brand-name">CLEARLINE TAX</div>

    <section class="services">
      <h2 class="services-heading">Specialising in</h2>
      <ul class="service-list">
        <li class="service-item"><svg class="service-tick" viewBox="0 0 20 20"><path d="M16.5,7.5 A8,8 0 1 1 13,3.2" fill="none" stroke="var(--accent-blue)" stroke-width="2.4" stroke-linecap="round"/><path d="M6,9.5 L9.5,13 L18,4" fill="none" stroke="var(--accent-blue)" stroke-width="2.4" stroke-linecap="round" stroke-linejoin="round"/></svg>Small Business Taxation</li>
        <li class="service-item"><svg class="service-tick" viewBox="0 0 20 20"><path d="M16.5,7.5 A8,8 0 1 1 13,3.2" fill="none" stroke="var(--accent-blue)" stroke-width="2.4" stroke-linecap="round"/><path d="M6,9.5 L9.5,13 L18,4" fill="none" stroke="var(--accent-blue)" stroke-width="2.4" stroke-linecap="round" stroke-linejoin="round"/></svg>Company &amp; Trust Returns</li>
        <li class="service-item"><svg class="service-tick" viewBox="0 0 20 20"><path d="M16.5,7.5 A8,8 0 1 1 13,3.2" fill="none" stroke="var(--accent-blue)" stroke-width="2.4" stroke-linecap="round"/><path d="M6,9.5 L9.5,13 L18,4" fill="none" stroke="var(--accent-blue)" stroke-width="2.4" stroke-linecap="round" stroke-linejoin="round"/></svg>Financial Statements</li>
        <li class="service-item"><svg class="service-tick" viewBox="0 0 20 20"><path d="M16.5,7.5 A8,8 0 1 1 13,3.2" fill="none" stroke="var(--accent-blue)" stroke-width="2.4" stroke-linecap="round"/><path d="M6,9.5 L9.5,13 L18,4" fill="none" stroke="var(--accent-blue)" stroke-width="2.4" stroke-linecap="round" stroke-linejoin="round"/></svg>Partnership Taxation</li>
        <li class="service-item"><svg class="service-tick" viewBox="0 0 20 20"><path d="M16.5,7.5 A8,8 0 1 1 13,3.2" fill="none" stroke="var(--accent-blue)" stroke-width="2.4" stroke-linecap="round"/><path d="M6,9.5 L9.5,13 L18,4" fill="none" stroke="var(--accent-blue)" stroke-width="2.4" stroke-linecap="round" stroke-linejoin="round"/></svg>BAS preparation/lodgement</li>
        <li class="service-item"><svg class="service-tick" viewBox="0 0 20 20"><path d="M16.5,7.5 A8,8 0 1 1 13,3.2" fill="none" stroke="var(--accent-blue)" stroke-width="2.4" stroke-linecap="round"/><path d="M6,9.5 L9.5,13 L18,4" fill="none" stroke="var(--accent-blue)" stroke-width="2.4" stroke-linecap="round" stroke-linejoin="round"/></svg>Capital Gains Tax</li>
        <li class="service-item"><svg class="service-tick" viewBox="0 0 20 20"><path d="M16.5,7.5 A8,8 0 1 1 13,3.2" fill="none" stroke="var(--accent-blue)" stroke-width="2.4" stroke-linecap="round"/><path d="M6,9.5 L9.5,13 L18,4" fill="none" stroke="var(--accent-blue)" stroke-width="2.4" stroke-linecap="round" stroke-linejoin="round"/></svg>Business Start Ups</li>
        <li class="service-item"><svg class="service-tick" viewBox="0 0 20 20"><path d="M16.5,7.5 A8,8 0 1 1 13,3.2" fill="none" stroke="var(--accent-blue)" stroke-width="2.4" stroke-linecap="round"/><path d="M6,9.5 L9.5,13 L18,4" fill="none" stroke="var(--accent-blue)" stroke-width="2.4" stroke-linecap="round" stroke-linejoin="round"/></svg>Business Structuring</li>
        <li class="service-item"><svg class="service-tick" viewBox="0 0 20 20"><path d="M16.5,7.5 A8,8 0 1 1 13,3.2" fill="none" stroke="var(--accent-blue)" stroke-width="2.4" stroke-linecap="round"/><path d="M6,9.5 L9.5,13 L18,4" fill="none" stroke="var(--accent-blue)" stroke-width="2.4" stroke-linecap="round" stroke-linejoin="round"/></svg>Tax Planning</li>
      </ul>
    </section>

    <div class="partner-badges">
      <div class="badge-listing" role="img" aria-label="Professional accreditation badge">
        <div class="badge-listing-main"></div>
        <div class="badge-listing-side"></div>
      </div>
      <div class="badge-software" role="img" aria-label="Accounting software partner badge"></div>
    </div>
  </div>
</body>
</html>
```